Vehicle Design

I would like the Van done with the logo and things that we do it need to look professional,
The link it to a car site for a 2003 KR Halden Corvex this is the same as i have so hope you can use the photos of here, or get the specs that you need, I have a sign person that does all my vehicles, so will need to pass the winning file to him,
Target Market(s)
mobile advertising police and housing
Industry/Entity Type
It Professional
Requirements
Must have
- logo, phone number 0455 873 316 what we do link attached,was hopping to have emblem on doors at rear, and sides done with style
Should be discrete but still make a noise
Nice to have
- Smoke that is in card that is attached
Should not have
- should not be too much not to scare clients from having me outside,

```html
<!DOCTYPE html>
<html lang="en">
<head>
<meta charset="utf-8">
<title>Clearwater Scene Restoration – Van Livery</title>
<link rel="stylesheet" href="https://fonts.googleapis.com/css2?family=Arimo:wght@400;700&display=swap">
<style>
  :root {
    --paper: #ffffff;
    --paper-shade: #d6d6d6;
    --floor: #3b3b3b;
    --floor-dark: #2a2a2a;
    --van-white: #ffffff;
    --van-line: #4a4a4a;
    --wrap-black: #1c1c1c;
    --wrap-grey: #3a3a3a;
    --trim: #5a5a5a;
    --glass: #8a8a8a;
    --tyre: #111111;
    --rim: #cfcfcf;
    --tape: #f5c400;
    --ink: #1a1a1a;
    --text-light: #ffffff;
    --lamp-amber: #f08a1c;
    --lamp-red: #d42a1e;
  }
  * { margin: 0; padding: 0; box-sizing: border-box; }
  html, body { width: 1200px; height: 620px; overflow: hidden; }
  body { font-family: "Arimo", Arial, sans-serif; }
  .livery-sheet { display: block; width: 1200px; height: 620px; }
  .phone-call { font-size: 19px; fill: var(--text-light); }
  .tape-text { font-size: 12px; font-weight: 700; fill: var(--ink); letter-spacing: 0.2px; }
  .service-list { font-size: 7.6px; fill: var(--text-light); }
  .service-list-rear { font-size: 6.8px; fill: var(--text-light); }
  .brand-name { font-weight: 700; font-size: 14px; fill: var(--ink); }
  .brand-name-rear { font-weight: 700; font-size: 10px; fill: var(--text-light); }
</style>
</head>
<body>
<svg class="livery-sheet" viewBox="0 0 1200 620" xmlns="http://www.w3.org/2000/svg">
  <defs>
    <linearGradient id="sky" x1="0" y1="0" x2="1" y2="1">
      <stop offset="0.35" stop-color="var(--paper)"/>
      <stop offset="1" stop-color="var(--paper-shade)"/>
    </linearGradient>
    <linearGradient id="floor" x1="0" y1="0" x2="0" y2="1">
      <stop offset="0" stop-color="var(--floor)"/>
      <stop offset="1" stop-color="var(--floor-dark)"/>
    </linearGradient>
    <linearGradient id="ground" x1="0" y1="0" x2="0" y2="1">
      <stop offset="0" stop-color="#e4e4e4"/>
      <stop offset="1" stop-color="#c9c9c9"/>
    </linearGradient>
    <radialGradient id="wrapGlow" cx="0.45" cy="0.4" r="0.7">
      <stop offset="0" stop-color="var(--wrap-grey)"/>
      <stop offset="1" stop-color="var(--wrap-black)"/>
    </radialGradient>
    <clipPath id="sideBody">
      <path d="M112 345 Q114 312 138 302 L205 262 L272 180 Q276 175 290 175 L752 176 Q768 178 770 192 L772 398 L112 398 Z"/>
    </clipPath>
  </defs>

  <!-- backdrop -->
  <rect class="backdrop-sky" width="1200" height="330" fill="url(#sky)"/>
  <rect class="backdrop-floor" y="328" width="1200" height="194" fill="url(#floor)"/>
  <rect class="backdrop-ground" y="522" width="1200" height="98" fill="url(#ground)"/>

  <!-- ===== side view ===== -->
  <g class="van-side">
    <g clip-path="url(#sideBody)">
      <rect class="side-panel" x="100" y="170" width="680" height="240" fill="var(--van-white)"/>
      <polygon class="side-wrap" points="356,400 556,176 780,176 780,400" fill="url(#wrapGlow)"/>
      <rect class="skirt" x="100" y="368" width="680" height="32" fill="var(--trim)"/>
    </g>
    <path class="body-outline" d="M112 345 Q114 312 138 302 L205 262 L272 180 Q276 175 290 175 L752 176 Q768 178 770 192 L772 398 L112 398 Z"
          fill="none" stroke="var(--van-line)" stroke-width="1"/>
    <path class="roof-line" d="M282 186 L760 186" stroke="var(--van-line)" stroke-width="0.8" fill="none"/>
    <path class="windscreen" d="M210 262 L274 186 L282 186 L226 262 Z" fill="var(--glass)"/>
    <path class="cab-window" d="M240 268 L282 220 L350 220 L350 290 L240 290 Z" fill="#6e6e6e" stroke="var(--van-line)" stroke-width="0.8"/>
    <path class="cab-door" d="M228 268 L228 372 M356 188 L356 372 M366 188 L366 372" stroke="var(--van-line)" stroke-width="0.8" fill="none"/>
    <rect class="door-handle" x="344" y="302" width="10" height="14" fill="var(--van-line)"/>
    <rect class="mirror" x="218" y="276" width="8" height="26" fill="var(--trim)"/>
    <path class="bumper" d="M108 335 L140 335 L140 392 L112 392 Z" fill="var(--trim)"/>
    <rect class="rear-bumper" x="760" y="374" width="30" height="20" fill="var(--trim)"/>
    <g class="wheels">
      <circle cx="216" cy="402" r="42" fill="var(--floor-dark)"/>
      <circle cx="216" cy="402" r="36" fill="var(--tyre)"/>
      <circle cx="216" cy="402" r="22" fill="var(--rim)"/>
      <circle cx="216" cy="402" r="8" fill="#9a9a9a"/>
      <circle cx="656" cy="402" r="42" fill="var(--floor-dark)"/>
      <circle cx="656" cy="402" r="36" fill="var(--tyre)"/>
      <circle cx="656" cy="402" r="22" fill="var(--rim)"/>
      <circle cx="656" cy="402" r="8" fill="#9a9a9a"/>
    </g>

    <rect class="body-outline-art" x="598" y="228" width="150" height="148" rx="60"
          fill="#2f2f2f" role="img" aria-label="Chalk body outline illustration"/>

    <rect class="police-tape" x="505" y="267" width="267" height="20" fill="var(--tape)"/>
    <text class="tape-text" x="640" y="281.5" text-anchor="middle">POLICE LINE DO NOT CROSS</text>

    <text class="phone-call" x="561" y="210">Call 0455 873 316</text>

    <text class="service-list" x="505" y="298">
      <tspan x="505" dy="0">Mould Inspections and Remediation</tspan>
      <tspan x="505" dy="9.6">Crime and Trauma Scene Cleanup and Decontamination</tspan>
      <tspan x="505" dy="9.6">Drug Lab Decontamination and Needle Cleanups</tspan>
      <tspan x="505" dy="9.6">Odour Control</tspan>
      <tspan x="505" dy="9.6">Air Quality Testing and Swabs</tspan>
      <tspan x="505" dy="9.6">Hydroxyl Machine, Ozone Machine, Sterilizing Light</tspan>
      <tspan x="505" dy="9.6">Comercial Steam Machines</tspan>
      <tspan x="505" dy="9.6">Thermal Imaging, Bacteria Testing</tspan>
    </text>

    <g class="brand-mark">
      <circle cx="382" cy="248" r="22" fill="var(--tape)"/>
      <text class="brand-name" x="382" y="292" text-anchor="middle">Clearwater</text>
      <text class="brand-name" x="382" y="310" text-anchor="middle">Scene</text>
      <text class="brand-name" x="382" y="328" text-anchor="middle">Restoration</text>
    </g>
  </g>

  <!-- ===== rear view ===== -->
  <g class="van-rear">
    <rect class="rear-mirror" x="808" y="282" width="20" height="28" rx="3" fill="var(--van-white)" stroke="var(--van-line)" stroke-width="0.6"/>
    <rect class="rear-mirror" x="1074" y="282" width="20" height="28" rx="3" fill="var(--van-white)" stroke="var(--van-line)" stroke-width="0.6"/>
    <rect class="rear-wheel" x="838" y="410" width="22" height="34" rx="3" fill="var(--tyre)"/>
    <rect class="rear-wheel" x="1042" y="410" width="22" height="34" rx="3" fill="var(--tyre)"/>
    <path class="rear-body" d="M834 190 Q836 176 852 175 L1050 175 Q1066 176 1068 190 L1070 398 L832 398 Z" fill="url(#wrapGlow)"/>
    <rect class="rear-bumper" x="828" y="392" width="246" height="28" rx="3" fill="var(--trim)"/>
    <g class="tail-lights">
      <rect x="834" y="325" width="16" height="14" fill="var(--lamp-amber)"/>
      <rect x="834" y="339" width="16" height="13" fill="var(--lamp-red)"/>
      <rect x="834" y="352" width="16" height="13" fill="#eeeeee"/>
      <rect x="1052" y="325" width="16" height="14" fill="var(--lamp-amber)"/>
      <rect x="1052" y="339" width="16" height="13" fill="var(--lamp-red)"/>
      <rect x="1052" y="352" width="16" height="13" fill="#eeeeee"/>
    </g>

    <text class="service-list-rear" x="868" y="189">
      <tspan x="868" dy="0">Mould Inspections and Remediation</tspan>
      <tspan x="868" dy="8.4">Crime and Trauma Scene Cleanup and Decontamination</tspan>
      <tspan x="868" dy="8.4">Drug Lab Decontamination and Needle Cleanups</tspan>
      <tspan x="868" dy="8.4">Odour Control</tspan>
      <tspan x="868" dy="8.4">Air Quality Testing and Swabs</tspan>
      <tspan x="868" dy="8.4">Hydroxyl Machine, Ozone Machine, Sterilizing Light</tspan>
      <tspan x="868" dy="8.4">Comercial Steam Machines</tspan>
      <tspan x="868" dy="8.4">Thermal Imaging, Bacteria Testing</tspan>
    </text>

    <rect class="body-outline-art" x="842" y="256" width="110" height="96" rx="40"
          fill="#2f2f2f" role="img" aria-label="Chalk body outline illustration"/>

    <rect class="police-tape" x="834" y="265" width="236" height="21" fill="var(--tape)"/>
    <text class="tape-text" x="864" y="280">POLICE LINE DO NOT CROSS</text>

    <rect class="plate" x="873" y="343" width="84" height="19" fill="var(--van-white)"/>

    <g class="brand-mark">
      <circle cx="1005" cy="306" r="14" fill="var(--tape)"/>
      <text class="brand-name-rear" x="1005" y="334" text-anchor="middle">Clearwater</text>
      <text class="brand-name-rear" x="1005" y="346" text-anchor="middle">Scene Restoration</text>
    </g>

    <text class="phone-call" x="872" y="383">Call 0455 873 316</text>
  </g>
</svg>
</body>
</html>
```